Website Design for Wheels for Troopers.org - Donated Cars to Disabled Vets

Need a Wordpress website. The coding now, esp. the CDONT coding is not supported by many hosting sites. Looking for a landing page to generate leads.

Logo Text

look at current one for ideas

Coding

Coded - Design and coding required

Number of Pages Required

1 page

Requirements
Must have
• look at current website at www.wheelsfortroopers.org
Nice to have
• look at this site: http://giftautotoheroes.org

```html
<!DOCTYPE html>
<html lang="en">
<head>
<meta charset="utf-8">
<title>Wheels for Troopers — Donate Your Car</title>
<link rel="stylesheet" href="https://fonts.googleapis.com/css2?family=Montserrat:wght@400;600;700&family=Open+Sans:wght@400;600&display=swap">
<style>
:root{
  --blue:#0b60c2;
  --blue-nav:#0a4f9f;
  --blue-tab:#1b72d6;
  --navy:#0b4590;
  --red:#d81410;
  --red-dark:#a8120e;
  --orange:#ff7a0a;
  --orange-btn:#ff8f12;
  --yellow:#eacb00;
  --ink:#333;
  --muted:#444;
  --grey-band:#efefef;
  --hero:#242424;
  --white:#fff;
}
*{margin:0;padding:0;box-sizing:border-box}
html,body{width:1103px;height:1200px;overflow:hidden;background:var(--white)}
body{position:relative;font-family:"Open Sans",Arial,sans-serif;color:var(--ink)}
.abs{position:absolute}
.head-font{font-family:"Montserrat",Arial,sans-serif}

.topbar{left:0;top:0;width:1103px;height:72px;background:var(--blue)}
.navbar{left:0;top:72px;width:1103px;height:46px;background:var(--blue-nav)}
.brand{left:158px;top:18px;display:flex;align-items:center;gap:8px;color:var(--white);font:600 17px "Montserrat",sans-serif}
.brand-dot{width:22px;height:22px;border-radius:50%;background:var(--red)}
.tagline{left:381px;top:26px;color:var(--white);font:600 11px "Montserrat",sans-serif}
.nav{left:188px;top:72px;display:flex;height:46px}
.nav a{color:var(--white);text-decoration:none;font:600 11px "Montserrat",sans-serif;display:flex;align-items:center;padding:0 13px}
.nav a.active{background:var(--blue-tab);padding:0 15px}

.hero{left:0;top:118px;width:1103px;height:407px;background:var(--hero)}
.hero-photo{left:150px;top:118px;width:700px;height:407px;background:radial-gradient(ellipse at 40% 55%,#6b5a48 0%,#3c3a38 45%,#242424 80%)}
.hero-copy{left:540px;top:436px;width:412px;text-align:center;color:#f4eee8;font:400 19px/22px "Montserrat",sans-serif}
.dots{left:888px;top:501px;display:flex;gap:8px}
.dots span{width:10px;height:10px;border-radius:50%;background:var(--red)}
.dots span:first-child{background:var(--white)}

.form-panel{left:690px;top:0;width:265px;height:395px;background:var(--red)}
.form-top{left:690px;top:0;width:265px}
.call{text-align:center;color:var(--white);width:265px;top:14px;left:0}
.call .l1{font:400 11.5px "Montserrat",sans-serif}
.call .num{font:700 24px/30px "Montserrat",sans-serif}
.call .l3{font:600 9px "Montserrat",sans-serif}
.field{left:721px;width:201px;height:23px;background:var(--white);font:600 7.5px "Montserrat",sans-serif;color:#555;padding:0 9px;display:flex;align-items:center;justify-content:space-between}
.btn-donate{left:774px;top:354px;width:94px;height:27px;background:var(--orange-btn);color:var(--white);font:400 11px "Montserrat",sans-serif;display:flex;align-items:center;justify-content:center}

.steps{left:149px;top:525px;width:806px;height:75px;display:flex}
.step{flex:1;display:flex;align-items:center;justify-content:center;gap:38px;color:var(--white);font:700 17px "Montserrat",sans-serif}
.step.call-us{background:var(--yellow)}
.step.tow{background:var(--orange)}
.step.tax{background:var(--red)}

.why-title{left:0;top:630px;width:1103px;text-align:center;color:var(--navy);font:700 21px "Montserrat",sans-serif}
.item{width:210px}
.item svg{position:absolute;left:-32px;top:2px}
.item h3{font:700 14px/17px "Montserrat",sans-serif;color:var(--ink)}
.item p{font:400 9px/11px "Open Sans",sans-serif;color:var(--muted);margin-top:3px;padding-left:2px;text-align:justify}

.cta{left:433px;top:856px;width:523px;height:68px;background:linear-gradient(100deg,#0a3f87 0%,#0a3f87 58%,#0c4b9a 58%,#0c4b9a 100%);color:var(--white);font:700 24px "Montserrat",sans-serif;display:flex;align-items:center;justify-content:center}

.trust{left:0;top:985px;width:690px;height:129px;background:var(--grey-band)}
.trust-title{left:178px;top:1037px;color:var(--navy);font:700 20px "Montserrat",sans-serif}
.program{left:690px;top:985px;width:413px;height:129px;background:var(--red)}
.program-text{left:722px;top:1023px;color:var(--white);font:700 20px/25px "Montserrat",sans-serif}
.program-arrow{left:902px;top:1026px;width:47px;height:43px;background:var(--orange-btn);border-radius:4px;display:flex;align-items:center;justify-content:center}

.social{left:169px;top:1133px;display:flex;gap:9px}
.social span{width:20px;height:20px;border-radius:2px}
.footer-nav{right:157px;top:1136px;display:flex;gap:26px;font:400 12px "Montserrat",sans-serif;color:var(--ink)}
.copy{right:157px;top:1165px;font:400 7.5px "Montserrat",sans-serif;color:var(--ink)}
</style>
</head>
<body>

<div class="abs topbar"></div>
<div class="abs navbar"></div>
<div class="abs brand"><span class="brand-dot"></span>Wheels for Troopers</div>
<div class="abs tagline">DONATE YOUR CAR TO A VET , MAKE A DIFFERENCE</div>
<nav class="abs nav">
  <a class="active">HOME</a><a>HOW IT WORKS</a><a>WHY DONATE YOUR CAR TO US?</a><a>FAQ</a>
</nav>

<div class="abs hero"></div>
<div class="abs hero-photo" role="img" aria-label="Smiling couple, a soldier holding a small US flag, with a hand offering car keys"></div>
<div class="abs hero-copy">DONATE YOUR CAR<br>FULL TAX DEDUCTION - RUNNING OR NOT</div>
<div class="abs dots"><span></span><span></span><span></span></div>

<div class="abs form-panel"></div>
<svg class="abs" style="left:690px;top:0" width="265" height="96" viewBox="0 0 265 96">
  <path d="M0 0H265V72L132 94L0 72Z" fill="var(--red-dark)"/>
</svg>
<div class="abs form-top">
  <div class="abs call">
    <div class="l1">CALL TODAY TO DONATE</div>
    <div class="num">1-800-555-0142</div>
    <div class="l3">Live Operators Available 7 Days a Week</div>
  </div>
</div>
<div class="abs field" style="top:110px">Name</div>
<div class="abs field" style="top:140px">Email</div>
<div class="abs field" style="top:170px">Phone Number</div>
<div class="abs field" style="top:201px">Cell Phone</div>
<div class="abs field" style="top:231px">Address</div>
<div class="abs field" style="top:262px">City</div>
<div class="abs field" style="top:292px">State<svg width="8" height="5"><path d="M0 0H8L4 5Z" fill="#222"/></svg></div>
<div class="abs field" style="top:322px">Zipcode</div>
<div class="abs btn-donate">DONATE NOW</div>

<div class="abs steps">
  <div class="step call-us">
    <svg width="20" height="20" viewBox="0 0 24 24"><path d="M6.6 10.8a15 15 0 0 0 6.6 6.6l2.2-2.2c.3-.3.7-.4 1-.2 1.1.4 2.3.6 3.6.6.6 0 1 .4 1 1V20c0 .6-.4 1-1 1C10.6 21 3 13.4 3 4c0-.6.4-1 1-1h3.5c.6 0 1 .4 1 1 0 1.3.2 2.5.6 3.6.1.3 0 .7-.2 1Z" fill="#fff"/></svg>
    CALL US</div>
  <div class="step tow">
    <svg width="22" height="24" viewBox="0 0 22 24" fill="none" stroke="#fff" stroke-width="1.6" stroke-linejoin="round"><path d="M7 12V4a1.5 1.5 0 0 1 3 0v7M10 10V2.5a1.5 1.5 0 0 1 3 0V10M13 10V3.5a1.5 1.5 0 0 1 3 0V11M16 11V6a1.5 1.5 0 0 1 3 0v9c0 4-3 7-7 7h-1c-3 0-4.5-2-6-4l-3-4.5a1.4 1.4 0 0 1 2.3-1.6L7 14"/></svg>
    WE TOW IT</div>
  <div class="step tax">
    <svg width="24" height="22" viewBox="0 0 24 22" fill="none" stroke="#fff" stroke-width="1.8"><path d="M14 4H4a2 2 0 0 0-2 2v12a2 2 0 0 0 2 2h12a2 2 0 0 0 2-2v-7"/><path d="M19 1l3 3-10 10H9v-3Z"/></svg>
    TAX WRITE OFF</div>
</div>

<div class="abs why-title">WHY DONATE YOUR CAR TO US?</div>

<svg width="0" height="0" style="position:absolute"><defs><symbol id="share-arrow" viewBox="0 0 16 13"><path d="M10 0l6 5.5L10 11V7.5C5 7.5 2.5 9 0 13c.5-5 3-9 10-9.5Z" fill="#333"/></symbol></defs></svg>

<div class="abs item" style="left:192px;top:690px"><svg width="15" height="13"><use href="#share-arrow"/></svg><h3>IRS 501(C)3 APPROVED</h3><p>Free 24/7 Pickup with No DMV Hassles.</p></div>
<div class="abs item" style="left:466px;top:690px"><svg width="15" height="13"><use href="#share-arrow"/></svg><h3>FREE LOCAL TOWING TO YOU</h3><p>We will pick up your car donation, running or not, when it's most convenient, at home or work.</p></div>
<div class="abs item" style="left:744px;top:690px;width:200px"><svg width="15" height="13"><use href="#share-arrow"/></svg><h3>ALL CARS ACCEPTED</h3><p>We take your car regardless of its condition or registration status.</p></div>

<div class="abs item" style="left:192px;top:774px;width:200px"><svg width="15" height="13"><use href="#share-arrow"/></svg><h3>INCOME TAX DEDUCTION</h3><p>We issue you an IRS tax receipt &amp; offer the largest resale network to get you the highest tax write-off possible.</p></div>
<div class="abs item" style="left:466px;top:774px;width:200px"><svg width="15" height="13"><use href="#share-arrow"/></svg><h3>NO PAPERWORK HASSLES</h3><p>We take any car and handle everything: DMV, Smog and IRS paperwork.</p></div>
<div class="abs item" style="left:744px;top:774px;width:200px"><svg width="15" height="13"><use href="#share-arrow"/></svg><h3>CAR DONATIONS HELP FUND PROGRAMS</h3><p>And benefit Troopers Mobility Fund. An IRS 501(c)3 nonprofit organization.</p></div>

<div class="abs item" style="left:192px;top:864px;width:200px"><svg width="15" height="13"><use href="#share-arrow"/></svg><h3>SCHEDULE A FREE PICKUP</h3><p>Complete the form and a representative will call you to arrange a convenient time to pickup your car.</p></div>

<div class="abs cta">DONATE YOUR CAR TODAY!</div>

<div class="abs trust"></div>
<div class="abs trust-title">SAFE &amp; SECURE</div>
<svg class="abs" style="left:392px;top:1022px" width="138" height="56" viewBox="0 0 138 56" aria-label="Security badge">
  <path d="M3 6L24 0l21 6v20c0 14-10 24-21 30C13 50 3 40 3 26Z" fill="#555"/>
  <rect x="54" y="12" width="82" height="32" rx="3" fill="#cfcfcf"/>
</svg>
<svg class="abs" style="left:578px;top:1016px" width="70" height="70" viewBox="0 0 70 70" aria-label="Charity approval badge">
  <circle cx="35" cy="35" r="34" fill="#4aa3d8"/><circle cx="35" cy="35" r="24" fill="#cfe3ef"/>
</svg>

<div class="abs program"></div>
<div class="abs program-text">CAR DONATION<br>PROGRAM</div>
<div class="abs program-arrow"><svg width="14" height="18" viewBox="0 0 14 18"><path d="M3 2l8 7-8 7" stroke="#fff" stroke-width="3.2" fill="none"/></svg></div>

<div class="abs social">
  <span style="background:#2e6fc4"></span><span style="background:#48a9e2"></span><span style="background:#6ab04c"></span><span style="background:#8a6a48"></span>
</div>
<div class="abs footer-nav"><span>HOME</span><span>HOW IT WORKS</span><span>WHY DONATE YOUR CAR TO US?</span><span>FAQ</span></div>
<div class="abs copy">© 2016 .www.companyname.com &nbsp;|&nbsp; All Rights Reserved.</div>

</body>
</html>
```